Business Card for beauty technology startup

Design Glowmi Business Card for a Beauty, based on the website identity and colors (https://www.glowmi-example.com).
Glowmi is a beauty tech startup that gathers helpful product info for beauty lovers and consumers (such as availability on stores, price range and product reviews) for makeup products. The card design must be young, colorful but clean, and very modern.

Target Market(s)

woman, 15-35

Industry/Entity Type

Cosmetics

Contact Information for Business Card

Full Name, address, phone

Font styles to use
Other font styles liked:
• Advent Pro

Colors
e34297
86cfc6
ffffff
5c5c5c
e8e8e8
e667a6
b2b2b2

Requirements
Must have
• One full colored side with a creative design and another with card info
• Use Color palette: #95C5C5 and/or #D38AA5
• Use fonts: Advent Pro
• Use website identity: https://www.glowmi-example.com
Nice to have
• If needed extra font: Roboto

```html
<!DOCTYPE html>
<html lang="en">
<head>
<meta charset="utf-8">
<title>Glowmi Business Card</title>
<link rel="stylesheet" href="https://fonts.googleapis.com/css2?family=Advent+Pro:wght@400;500;600&display=swap">
<style>
  :root {
    --stage: #0b0b0b;
    --card-white: #ffffff;
    --brand-pink: #c47a97;
    --back-pink: #d38aa5;
    --band-pink: #e2abc0;
    --ink-grey: #5c5c5c;
    --rule-grey: #8a8a8a;
  }
  * { box-sizing: border-box; margin: 0; padding: 0; }
  html, body {
    width: 1200px; height: 1000px; overflow: hidden;
    background: var(--stage);
    font-family: "Advent Pro", sans-serif;
  }
  .canvas { position: relative; width: 1200px; height: 1000px; }
  .card {
    position: absolute; width: 520px; height: 300px;
    border-radius: 26px; overflow: hidden;
  }
  .card-front { left: 70px; top: 180px; background: var(--card-white); }
  .card-back { left: 610px; top: 500px; background: var(--back-pink); }

  .brand { position: absolute; left: 46px; top: 44px; display: flex; align-items: center; gap: 14px; }
  .brand-dot { width: 30px; height: 30px; border: 2px solid var(--brand-pink); border-radius: 50%; }
  .brand-name {
    color: var(--brand-pink); font-size: 30px; font-weight: 400;
    letter-spacing: 6px; text-transform: uppercase;
  }
  .rule { position: absolute; height: 2px; }
  .rule-grey { left: 40px; top: 100px; width: 250px; background: var(--rule-grey); }
  .rule-pink { left: 250px; top: 168px; width: 230px; background: var(--brand-pink); }

  .address { position: absolute; left: 48px; top: 120px; color: var(--ink-grey); font-size: 17px; line-height: 1.25; }
  .person { position: absolute; left: 320px; top: 112px; }
  .person-name { color: var(--brand-pink); font-size: 24px; font-weight: 500; line-height: 1.1; }
  .person-role { color: var(--ink-grey); font-size: 18px; line-height: 1.1; }
  .contact { position: absolute; left: 300px; top: 186px; color: var(--ink-grey); font-size: 17px; line-height: 1.3; }

  .pattern-band { position: absolute; inset: 0; }
  .back-mark {
    position: absolute; left: 185px; top: 75px; width: 150px; height: 150px;
    border-radius: 50%; background: var(--card-white);
    display: flex; align-items: center; justify-content: center;
  }
  .back-mark-name { color: var(--brand-pink); font-size: 30px; font-weight: 500; letter-spacing: 2px; }
</style>
</head>
<body>
<main class="canvas">
  <section class="card card-front">
    <div class="brand">
      <span class="brand-dot"></span>
      <span class="brand-name">Glowmi</span>
    </div>
    <div class="rule rule-grey"></div>
    <div class="rule rule-pink"></div>
    <p class="address">12 Harbor Lane<br>Eastfield, IL 60000</p>
    <div class="person">
      <p class="person-name">Mira Lane</p>
      <p class="person-role">owner</p>
    </div>
    <p class="contact">55 210 7788<br>www.glowmi-example.com</p>
  </section>

  <section class="card card-back">
    <svg class="pattern-band" width="520" height="300" viewBox="0 0 520 300" role="img" aria-label="Diagonal band of white dashed lines">
      <polygon points="60,0 330,0 470,300 200,300" fill="var(--band-pink)"/>
    </svg>
    <div class="back-mark">
      <span class="back-mark-name">Glowmi</span>
    </div>
  </section>
</main>
</body>
</html>
```